Modern Lawfirm Business Card Design

We're looking for a business card to incorporate the newly created logo we had made.

Ideally looking for a law firm business card demonstrating, modern, minimalist, strong/bold design.

I'm open to any design honestly, but nothing "flashy".

Target Market(s)

Immigration law, family immigration, humanitarian, general legal

Industry/Entity Type

Law Firm

Contact Information for Business Card

Please use dummy information, name, street address, city, state, phone number, email, website.

Font styles to use
Serif
Sans Serif

Requirements
Must have
• Please use dummy information, name, street address, city, state, phone number, email, website.

```html
<!DOCTYPE html>
<html lang="en">
<head>
<meta charset="utf-8">
<title>Calloway – Business Card</title>
<link href="https://fonts.googleapis.com/css2?family=Source+Sans+3:ital,wght@0,400;0,600;0,700;1,400&display=swap" rel="stylesheet">
<style>
  :root {
    --page: #ffffff;
    --navy-deep: #0a1a3f;
    --navy: #1b3670;
    --band: #2a5096;
    --band-light: #5a73b4;
    --paper: #eceef7;
    --paper-light: #f5f6fb;
    --plate: #f1f2f8;
    --ink: #2b2b2f;
    --accent: #2d4a8a;
    --icon: #0d4f9e;
    --white: #ffffff;
  }
  * { margin: 0; padding: 0; box-sizing: border-box; }
  html, body { width: 1200px; height: 1000px; overflow: hidden; background: var(--page); }
  body { position: relative; font-family: "Source Sans 3", sans-serif; }

  .card {
    position: absolute; left: 36px; top: 177px; width: 1125px; height: 675px;
    background: var(--paper); overflow: hidden;
  }
  .card-art {
    position: absolute; left: 0; top: 0; width: 1125px; height: 348px;
    background: radial-gradient(ellipse at 40% 30%, #3a5a9e 0%, var(--navy) 45%, var(--navy-deep) 100%);
  }
  .paper-texture {
    position: absolute; left: 0; top: 348px; width: 1125px; height: 327px;
    background: linear-gradient(180deg, var(--paper) 0%, var(--paper-light) 100%);
  }
  .shapes { position: absolute; left: 0; top: 0; }

  .firm-plate {
    position: absolute; left: 344px; top: 138px; width: 449px; height: 118px;
    background: var(--plate);
    display: flex; align-items: center; justify-content: center;
  }
  .firm-name {
    color: var(--navy); font-weight: 600; font-size: 64px;
    letter-spacing: 4px; line-height: 1;
  }
  .address {
    position: absolute; left: 0; width: 1125px; top: 360px;
    text-align: center; color: var(--white); font-size: 21px;
  }

  .person { position: absolute; right: 663px; top: 486px; text-align: right; }
  .person-name { font-size: 37px; color: var(--ink); font-weight: 400; line-height: 1; letter-spacing: -0.5px; }
  .person-name strong { font-weight: 700; }
  .person-title { font-style: italic; font-size: 24px; color: var(--accent); margin-top: 2px; }

  .divider { position: absolute; left: 561px; top: 460px; width: 3px; height: 123px; background: var(--accent); }

  .contacts { position: absolute; left: 664px; top: 460px; list-style: none; }
  .contacts li { display: flex; align-items: center; height: 35px; margin-bottom: 9px; font-size: 22px; color: var(--ink); }
  .contacts .icon { width: 35px; height: 35px; margin-right: 16px; flex: none; }
</style>
</head>
<body>
  <div class="card">
    <div class="card-art" role="img" aria-label="Abstract deep-blue background with soft light streaks and curves"></div>
    <div class="paper-texture" role="img" aria-label="Faint pale lavender textured backdrop"></div>

    <svg class="shapes" width="1125" height="675" viewBox="0 0 1125 675" aria-hidden="true">
      <polygon points="269,188 884,188 951,256 205,256" fill="var(--band-light)" opacity="0.55"/>
      <rect x="0" y="348" width="1125" height="43" fill="var(--paper-light)" opacity="0.85"/>
      <polygon points="217,340 944,340 889,408 274,408" fill="var(--band)"/>
    </svg>

    <div class="firm-plate"><div class="firm-name">CALLOWAY</div></div>
    <div class="address">412 Harbor Lane Brookvale NY 6789</div>

    <div class="person">
      <div class="person-name"><strong>JOHN</strong> DOE</div>
      <div class="person-title">immigration lawyer</div>
    </div>

    <div class="divider"></div>

    <ul class="contacts">
      <li>
        <svg class="icon" viewBox="0 0 35 35" aria-hidden="true">
          <circle cx="17.5" cy="17.5" r="17.5" fill="var(--icon)"/>
          <path d="M9 14 q8.5 -6 17 0 v2 h-4 v-2 h-9 v2 h-4 z" fill="#fff"/>
          <rect x="11" y="17" width="13" height="8" rx="1" fill="#fff"/>
        </svg>
        000 . 0000. 4821
      </li>
      <li>
        <svg class="icon" viewBox="0 0 35 35" aria-hidden="true">
          <circle cx="17.5" cy="17.5" r="17.5" fill="var(--icon)"/>
          <rect x="8.5" y="11" width="18" height="13" fill="#fff"/>
          <path d="M8.5 11 l9 7 l9 -7 M8.5 24 l6.5 -6 M26.5 24 l-6.5 -6" stroke="var(--icon)" stroke-width="1.2" fill="none"/>
        </svg>
        jdoe@callowaylaw.com
      </li>
      <li>
        <svg class="icon" viewBox="0 0 35 35" aria-hidden="true">
          <circle cx="17.5" cy="17.5" r="17.5" fill="var(--icon)"/>
          <rect x="8.5" y="9.5" width="18" height="12.5" fill="#fff"/>
          <rect x="10.5" y="11.5" width="14" height="8.5" fill="var(--icon)"/>
          <rect x="16" y="22" width="3" height="3" fill="#fff"/>
          <rect x="12" y="25" width="11" height="2" fill="#fff"/>
        </svg>
        callowaylaw.com
      </li>
    </ul>
  </div>
</body>
</html>
```